we are an outdoor outlet in a country club that has a variety of outlets. The Club is called Larkmoor and is located in Cairo, Egypt. This garden menu will include cuisines from the Mediterranean, Asia and Texmex. we need a menu that is colorful and would fit an A3 size, back and front are to be used. Attached is the old menu currently in use (Garden Menu 2012.pdf is just for reference) and the new menu text for you to use is under the name Garden Menu Fall 2013
thank you.

```html
<!DOCTYPE html>
<html lang="en">
<head>
<meta charset="utf-8">
<title>Larkmoor Garden Menu – Fall 2013</title>
<link rel="stylesheet" href="https://fonts.googleapis.com/css2?family=PT+Sans+Narrow:wght@400;700&family=Didact+Gothic&family=Open+Sans:ital,wght@0,400;1,400&display=swap">
<style>
  :root{
    --brown:#4a2410;
    --lime:#c8c82c;
    --orange:#d4581e;
    --ink:#1c1c1c;
    --paper:#ffffff;
  }
  *{box-sizing:border-box;margin:0;padding:0}
  html,body{width:1200px;height:1000px;overflow:hidden;background:var(--paper)}
  .menu{position:relative;width:1200px;height:1000px;background:var(--paper);color:var(--ink);font-family:"Didact Gothic",sans-serif}
  .bar-side{position:absolute;top:20px;width:12px;height:956px;background:var(--brown)}
  .bar-side.left{left:0}
  .bar-side.right{right:0;width:10px}
  .band{position:absolute;left:28px;width:1148px;height:23px;background:var(--lime)}
  .band.top{top:22px}
  .band.bottom{top:955px}
  .frame{position:absolute;left:15px;top:52px;width:1168px;height:893px;border:1.5px solid var(--orange)}

  .title{position:absolute;right:48px;top:64px;font-family:"PT Sans Narrow",sans-serif;font-weight:700;font-size:46px;color:var(--brown);letter-spacing:.2px;white-space:nowrap}
  .corner{position:absolute;font-family:"PT Sans Narrow",sans-serif;font-weight:400;font-size:23px;color:var(--brown);line-height:1;white-space:nowrap}
  .section{position:absolute}
  .section h3{font-family:"Didact Gothic",sans-serif;font-weight:400;font-size:16px;letter-spacing:1px;color:var(--ink)}
  .section p{white-space:nowrap}
  .price,.desc{font-style:italic}

  .left p{font-size:13px;letter-spacing:1.05px;line-height:14.6px}
  .left .desc{padding-left:26px}
  .left .apps p{line-height:15.6px}
  .left .salads p{line-height:16.8px}
  .left .pasta p{line-height:17.4px}

  .right{font-family:"Open Sans",sans-serif}
  .right h3{margin-bottom:3px}
  .right p{font-size:9.8px;line-height:18.4px}
  .right .desc{padding-left:19px;font-size:9.2px;letter-spacing:.2px}
  .right .plain{padding-left:19px;font-style:normal;font-size:10.2px}
  .right .price{font-size:11px;margin-left:8px}

  .brand{position:absolute;left:430px;top:838px;width:350px;text-align:center;font-family:"Didact Gothic",sans-serif;font-size:34px;color:var(--brown);white-space:nowrap}
  .season{position:absolute;left:586px;top:912px;font-family:"PT Sans Narrow",sans-serif;font-weight:700;font-size:18px;color:var(--brown)}
  .note{position:absolute;right:42px;top:920px;font-family:"Open Sans",sans-serif;font-style:italic;font-size:11px;letter-spacing:1.3px;color:var(--ink);white-space:nowrap}
</style>
</head>
<body>
<div class="menu">
  <div class="bar-side left"></div>
  <div class="bar-side right"></div>
  <div class="band top"></div>
  <div class="band bottom"></div>
  <div class="frame"></div>

  <h1 class="title">Garden Menu</h1>

  <h2 class="corner" style="left:30px;top:117px">Mediterranean Corner</h2>
  <div class="left">
    <div class="section" style="left:60px;top:136px"><h3>Soups:</h3></div>
    <div class="section" style="left:66px;top:155px">
      <p>Tomato Basil <span class="price">(price)</span></p>
      <p class="desc">Simmered tomato soup finished with fresh basil and cream</p>
      <p>Chicken Cream <span class="price">(price)</span></p>
      <p class="desc">Chicken broth with roasted chicken cubes, pine nuts, and cream</p>
      <p>Moroccan Harira <span class="price">(price)</span></p>
      <p class="desc">Vegetable broth with fresh tomato, chickpeas, lentil, cilantro, diced lamb</p>
    </div>

    <div class="section" style="left:62px;top:261px"><h3>Appetizers:</h3></div>
    <div class="section apps" style="left:62px;top:280px">
      <p>Salmon Tartre season <i>with lemon juice, garlic and crushedblack pepper</i> <span class="price">(price)</span></p>
      <p>Roasted Eggplant Rolls <i>with herbed ricotta cheese and pine nuts</i> <span class="price">(price)</span></p>
      <p>Falafel in Mini Pita served with tehina and oriental salsa <span class="price">(price)</span></p>
      <p>Mankousha with thyme and olive oil <span class="price">(price)</span></p>
      <p>Fried kobeba with minced meat, spices, and pine nuts <span class="price">(price)</span></p>
      <p>Fried calamari a la Romana served with aioli <span class="price">(price)</span></p>
      <p>Samboussek with herbed white cheese and mint <span class="price">(price)</span></p>
      <p>Oriental sausage sautéed with garlic and onion <span class="price">(price)</span></p>
      <p>Mini vine leaves with a yoghurt dip <span class="price">(price)</span></p>
      <p>Fatouch with a pomegranate syrup dressing <span class="price">(price)</span></p>
      <p>Hummus seasoned with lemon juice, garlic, and olive oil <span class="price">(price)</span></p>
      <p>White cheese with diced tomato, thyme, and olive oil <span class="price">(price)</span></p>
      <p>Tehina seasoned with cumin, lemon juice, and garlic <span class="price">(price)</span></p>
    </div>

    <div class="section" style="left:60px;top:500px"><h3>Salads:</h3></div>
    <div class="section salads" style="left:62px;top:519px">
      <p>Caprese <span class="price">(price)</span></p>
      <p class="desc">Buffalo mozzarella and sliced tomato with a balsamic vinaigrette</p>
      <p>Rocket Apple <span class="price">(price)</span></p>
      <p class="desc">Rocket leaves with gorgonzola, croutons, and strawberry vinaigrette</p>
      <p>French Riviera Nicoise <span class="price">(price)</span></p>
      <p class="desc">Lettuce, egg, tomato, tuna, olives, onion, celery, radish, bell pepper in a<br>French vinaigrette</p>
      <p>Folle <span class="price">(price)</span></p>
      <p class="desc">Mixed greens with crab sticks, mushroom, corn, cherry tomato in a<br>mango vinaigrette</p>
    </div>

    <div class="section" style="left:62px;top:694px"><h3>Pizza &amp; Pasta:</h3></div>
    <div class="section pasta" style="left:62px;top:713px">
      <p>Pizza Margarita (Choose your toppings) <span class="price">(price)</span></p>
      <p>Create your own pasta</p>
      <p>Type&nbsp; Spaghetti, Tagliatelle, Penne</p>
      <p>Sauces: Napolitana, Bolognese, Alfredo</p>
      <p>Toppings:</p>
      <p>Bell peppers, olives, tomato, onion</p>
      <p>Mushroom, chicken, tuna, pepperoni</p>
      <p>Smoked salmon, shrimps</p>
      <p>Lasagna <span class="price">(price)</span></p>
    </div>

    <div class="section" style="left:62px;top:878px"><h3>Sandwiches:</h3></div>
    <div class="section" style="left:62px;top:898px">
      <p>(Served with French fries or a garden salad)</p>
      <p>Beef or chicken Shawerma <span class="price">(price)</span></p>
    </div>
  </div>

  <h2 class="corner" style="left:665px;top:116px">Asian Corner</h2>
  <div class="right">
    <div class="section" style="left:697px;top:134px">
      <h3>Salads &amp; Appetizers:</h3>
      <p>Chicken Wasabi Salad <span class="price">(price)</span></p>
      <p class="desc">Diced chicken with a mayo wasabi dressing on top of shredded lettuce</p>
      <p>Chicken Sesame Noodle Salad <span class="price">(price)</span></p>
      <p class="desc">Sesame crusted chicken with glass noodles tossed with sweet chili, soy sauce, and lemongrass</p>
      <p>Spring rolls <span class="price">(price)</span></p>
      <p class="desc">Vegetable spring rolls served with house made sweet and sour dip</p>
      <p>Indian Samosa <span class="price">(price)</span></p>
      <p class="desc">Fried dough parcels filled with vegetables and spices</p>
    </div>
    <div class="section" style="left:697px;top:312px">
      <h3>Main Courses:</h3>
      <p>Murgh Chicken Makhni <span class="price">(price)</span></p>
      <p class="plain">Chicken cubes in a rich creamy tomato sauce seasoned with garam masala</p>
      <p class="plain">Choice of side: vegetable korma or curd</p>
      <p>Chicken Tandoori <span class="price">(price)</span></p>
      <p class="plain">Grilled chicken cubes with tandoori spices served with basmati rice</p>
      <p>Thai Coconut Curry Shrimp <span class="price">(price)</span></p>
      <p class="plain" style="line-height:12px">Sautéed shrimp tossed with curry and coconut milk served with jasmine rice</p>
      <p style="line-height:14px">Mongolian Beef <span class="price">(price)</span></p>
      <p class="plain">Soy marinated beef with oyster sauce and vegetables served with egg noodles</p>
    </div>

    <h2 class="corner" style="left:660px;top:506px">Tex Mex</h2>
    <div class="section" style="left:697px;top:525px">
      <h3>Salads &amp; Appetizers:</h3>
      <p>Caesar Salad <span class="price">(price)</span></p>
      <p class="desc">Iceberg lettuce with Caesar dressing with grated Parmesan cheese and croutons</p>
      <p>Taco Salad 42 <span class="price">(price)</span></p>
      <p class="desc">Chicken breast, beans, sour cream, guacamole, tomato, corn, lettuce, olives, chives, vinaigrette</p>
      <p>Nachos topped with chili, melted cheese, beans <span class="price">(price)</span></p>
      <p>Chicken Quesadilla served with guacamole, salsa, and sour cream <span class="price">(price)</span></p>
    </div>
    <div class="section" style="left:697px;top:670px">
      <h3>Main Courses &amp; Sandwiches:</h3>
      <p>Cheeseburge <span class="price">(price)</span></p>
      <p class="desc">House made lean beef burger topped with cheddar cheese</p>
      <p>Mushroom Burger <span class="price">(price)</span></p>
      <p class="desc">Beef burger with sautéed mushroom, caramelized onion, and provolone cheese</p>
      <p>Crispy Chicken Wrap <span class="price">(price)</span></p>
      <p class="desc">Crisp fried chicken wrap with a ranch dressing</p>
      <p>Fajita <i>(Chicken, Beef, Combo)</i> <span class="price">(price)</span></p>
    </div>
  </div>

  <p class="brand">Larkmoor Country Club</p>
  <div class="season">Fall 2013</div>
  <p class="note">**Prices are subject to 12% service charge and 10% sales tax**</p>
</div>
</body>
</html>
```